Gilded Reef / Alcoholic Drink, Brochure design

We are in need of a design for our all natural, low calorie, organically sweetened alcoholic drink. Our drink is currently a frozen mixed drink similar to a margarita and has the taste of real fruit. It is targeted to high end, midrange, and lower end resorts and hotels through Mexico. It will eventually enter the U.S. market within one year in the form of both the frozen and canned and bottled ready to drink. Some things to include in the brochure are:

Welcome to the harmonious and flavorful, world of Gilded Reef. Encounter the bold, real fruit taste of an exceptional drink that is organically sweetened, all natural, low in calories with a refreshing, smooth finish. Gilded Reef uses ultra premium ingredients and distilled by a process so pure, that it delivers a smooth, full, balanced taste with no bitter after burn. So, on hot summer days and steamy nights join us for the one of a kind experience of Gilded Reef.

-All Natural, real fruit
-Organically sweetened
-Low Calorie
-Bottled at the Source
-Solid revenues
-High profit margin

Target Market(s)

Resort managers, purchasers. Their market is 25-50 age range males and females who vacation at cities in Mexico like Cancun, Puerta Vallarta.

Font styles to use
Sans Serif

Requirements
Must have
• Clean, modern, upscale design
• Why you should consider Gilded Reef for your business. In the rapidly growing market of organic foods and healthy choices, Gilded Reef is a leader in the alcohol industry on this phenomena. Our ultra premium, all natural, low calorie ingredients are perfect for this exponentially expanding market in the U.S., Europe and beyond. Whether your establishment is a corporate all inclusive resort destination, a midrange one or just one owned by an individual, we've designed Gilded Reef to keep you within a highly profitable margin - thus making you money.
• Frozen-
• Crafted and bottled at the source.
• No guesswork in adding liquor, just pour, freeze and serve.
• A large selection of real fruit flavors.
• Two different ABV percentages to choose from 5% and "Gilded Summit" at 8%.
• Ready to Drink-
• Crafted and bottled at the source
• Carbonated for the ultimate in refreshment
• Available in both glass and aluminum

```html
<!DOCTYPE html>
<html lang="en">
<head>
<meta charset="utf-8">
<title>Gilded Reef – Brochure</title>
<link href="https://fonts.googleapis.com/css2?family=Questrial&family=Mulish:ital,wght@0,400;0,700;0,800;1,400;1,700;1,800&family=Montserrat:wght@700;800&display=swap" rel="stylesheet">
<style>
:root{
  --sky:#5bbde6;
  --brand-blue:#1b86c2;
  --ink:#262626;
  --violet:#3a2c86;
  --sun-red:#e5302a;
  --leaf-green:#2c8a2f;
  --stone:#7d7d7d;
  --white:#ffffff;
}
*{margin:0;padding:0;box-sizing:border-box}
html,body{width:1200px;height:933px;overflow:hidden;background:var(--sky)}
.brochure{position:relative;width:1200px;height:933px;background:var(--sky);font-family:"Questrial",sans-serif;color:var(--ink)}
.hero{position:absolute;left:0;top:0;width:1200px;height:933px}
.brand-mark{position:absolute;left:1060px;top:360px;display:flex;align-items:center;gap:8px;font-family:"Questrial",sans-serif;font-size:19px;color:var(--white)}
.brand-mark .dot{width:12px;height:12px;border-radius:50%;background:var(--white)}

.pitch{position:absolute;left:34px;top:402px;width:340px}
.pitch h2{font-family:"Questrial",sans-serif;font-weight:400;font-size:29px;line-height:36.5px;color:#111;text-transform:uppercase;letter-spacing:.2px}
.pitch h2 strong{font-family:"Montserrat",sans-serif;font-weight:800}
.pitch p{font-size:14.5px;line-height:20px;margin-top:28px}
.pitch .claim{font-family:"Mulish",sans-serif;font-style:italic;font-weight:800;font-variant:small-caps;color:var(--violet);text-align:center;font-size:14px;line-height:21px;margin-top:6px;padding:0 6px}
.pitch .claim + p{margin-top:6px}

.welcome{position:absolute;left:427px;top:470px;width:350px;height:436px;background:rgba(255,255,255,.86);text-align:center;padding:16px 10px 0}
.welcome h1{font-family:"Questrial",sans-serif;font-weight:400;font-size:29px;line-height:27px;color:#111;text-transform:uppercase}
.welcome h1 b{font-family:"Montserrat",sans-serif;font-weight:700;font-size:27px}
.welcome h1 .tone-blue{color:var(--brand-blue)}
.welcome h1 .tone-grey{color:var(--stone)}
.welcome p{font-size:14.5px;line-height:20px;margin-top:18px;padding:0 6px}
.welcome .invite{font-family:"Mulish",sans-serif;font-style:italic;font-weight:800;font-size:15.5px;line-height:24px;margin-top:2px}
.invite .hot{color:var(--sun-red)}
.invite .steamy{color:var(--leaf-green)}
.invite .tone-blue{color:var(--brand-blue)}
.invite .tone-grey{color:var(--stone)}

.range-title{position:absolute;background:var(--white);font-family:"Montserrat",sans-serif;font-weight:800;color:var(--brand-blue);font-size:28px;text-align:center;line-height:50px;height:50px;letter-spacing:.5px}
.range-title.frozen{left:918px;top:434px;width:165px}
.range-title.ready{left:850px;top:671px;width:302px}
.features{position:absolute;list-style:none;font-family:"Mulish",sans-serif;font-style:italic;font-size:15px;line-height:26px;color:#1d1d1d}
.features li{position:relative;padding-left:29px}
.features li::before{content:"";position:absolute;left:0;top:9px;width:7px;height:7px;border-radius:50%;background:var(--white)}
.features b{font-weight:800}
.features.frozen{left:824px;top:499px;width:360px}
.features.ready{left:826px;top:740px;width:360px}
.features .wrap{line-height:22px;padding-bottom:4px}
</style>
</head>
<body>
<main class="brochure">
  <svg class="hero" viewBox="0 0 1200 933" aria-hidden="false">
    <defs>
      <linearGradient id="nightGlow" x1="0" y1="0" x2="1" y2="0.3">
        <stop offset="0" stop-color="#4a4130"/>
        <stop offset="0.45" stop-color="#5a4a35"/>
        <stop offset="0.8" stop-color="#7a4a5a"/>
        <stop offset="1" stop-color="#a0587a"/>
      </linearGradient>
    </defs>
    <polygon role="img" aria-label="Photo of young friends in swimwear walking at night holding bottles of the drink" points="0,0 1200,0 1200,128 808,500 432,500 0,148" fill="url(#nightGlow)"/>
  </svg>

  <div class="brand-mark"><span class="dot"></span>Gilded Reef</div>

  <section class="pitch">
    <h2>Why<br>you should<br>consider <strong>GR</strong><br>for your company</h2>
    <p>In the rapidly growing market of organic foods and healthy choices, GR is a leader in the alcohol industry on this phenomena.</p>
    <p class="claim">Our ultra premium, all natural, low calorie ingredients are perfect for this exponentially expanding market in the U.S., Europe and beyond.</p>
    <p>Whether your establishment is a corporate all inclusive resort destination, a midrange one or just one owned by an individual, we've designed Gilded Reef to keep you within a highly profitable margin - thus making you money.</p>
  </section>

  <section class="welcome">
    <h1>Welcome <b>to the harmonious and flavorful, world of</b> <b class="tone-blue">Gilded</b> <b class="tone-grey">Reef.</b></h1>
    <p>Encounter the bold, real fruit taste of an exceptional drink that is organically sweetened, all natural, low in calories with a refreshing, smooth finish.</p>
    <p>Gilded Reef uses ultra premium ingredients and distilled by a process so pure, that it delivers a smooth, full, balanced taste with no bitter after burn.</p>
    <p class="invite">So, on <span class="hot">hot summer days</span> and <span class="steamy">steamy nights</span> join us for the one of a kind experience of <span class="tone-blue">Gilded</span> <span class="tone-grey">Reef.</span></p>
  </section>

  <div class="range-title frozen">FROZEN</div>
  <ul class="features frozen">
    <li>Crafted and bottled <b>at the source.</b></li>
    <li class="wrap"><b>No guesswork</b> in adding liquor, just pour,<br>freeze and serve.</li>
    <li>A large selection of <b>real fruit</b> flavors.</li>
    <li><b>Two different</b> ABV percentages to choose<br>from 5% and "Gilded Summit" at 8%.</li>
  </ul>

  <div class="range-title ready">READY TO DRINK</div>
  <ul class="features ready">
    <li>Crafted and bottled <b>at the source.</b></li>
    <li class="wrap"><b>Carbonated</b> for the ultimate<br>in refreshment</li>
    <li>Available in both <b>glass and aluminum</b></li>
    <li><b>Two different</b> ABV percentages to choose<br>from 5% and "Gilded Summit" at 8%.</li>
  </ul>
</main>
</body>
</html>
```